****Business Card Design for Cormwell Development. Design based around attached logo/company name

I’m looking for business card design for my company Cormwell Development Group,LLC. Design should be professional, sharp and minimal. Outside of the attached logos, greyscale colors for remainder of cards. My thoughts are two-sided card with attached logo on one side and my info on the other but open to one-sided as well with right design.
Target Market(s)
Real estate professionals including banks, private investors, property owners, developers, commercial tenants like Brewlantic, Granvey or Tamsett’s.
Industry/Entity Type
Commercial real estate development and investments.
Contact Information for Business Card
Name, title, email, phone #’s, web address and physical address
Font styles to use
Other font styles liked:
- Helvetica, Garamond, etc
Colors
Designer to choose only greyscale colors for use in the design.
Requirements
Must have
- Attached logo first or second options.
Nice to have
- Two sided card with logo on one side. Attached Logo/company name can be laid out any way that flows as long as it’s legible.name
Should not have
- No loud colors. ***Please do not include logo, I have removed the company design with a logo image.

```html
<!DOCTYPE html>
<html lang="en">
<head>
<meta charset="utf-8">
<title>Cormwell Development Group, LLC — Business Card</title>
<link href="https://fonts.googleapis.com/css2?family=Lato:wght@400&family=Roboto:wght@400&display=swap" rel="stylesheet">
<style>
  :root {
    --backdrop: #9a9c9b;
    --card: #5e6474;
    --ink: #ffffff;
    --rule: #e9ebef;
  }
  * { margin: 0; padding: 0; box-sizing: border-box; }
  html, body { width: 1200px; height: 1200px; overflow: hidden; }
  body { background: var(--backdrop); position: relative; font-family: "Lato", sans-serif; color: var(--ink); }

  .card { position: absolute; left: 232px; width: 736px; height: 452px; background: var(--card); }
  .card--front { top: 116px; }
  .card--back { top: 632px; }

  .wordmark { position: absolute; font-family: "Lato", sans-serif; font-weight: 400; color: var(--ink); letter-spacing: 0.08em; line-height: 1; }
  .wordmark__line { display: block; white-space: nowrap; }
  .card--front .wordmark { left: 128px; top: 66px; }
  .card--front .wordmark__name { font-size: 40px; }
  .card--front .wordmark__sub { font-size: 15px; margin-top: 10px; letter-spacing: 0.1em; }
  .card--back .wordmark { left: 200px; top: 160px; }
  .card--back .wordmark__name { font-size: 78px; }
  .card--back .wordmark__sub { font-size: 27px; margin-top: 18px; letter-spacing: 0.1em; }

  .holder { position: absolute; right: 42px; top: 182px; text-align: right; font-family: "Roboto", sans-serif; }
  .holder__name { font-size: 35px; line-height: 42px; }
  .holder__title { font-size: 22px; line-height: 28px; }

  .divider { position: absolute; left: 44px; top: 265px; width: 649px; height: 2px; background: var(--rule); }

  .contacts { position: absolute; left: 42px; top: 288px; list-style: none; }
  .contacts__item { display: flex; align-items: center; height: 30.5px; font-size: 20px; }
  .contacts__icon { width: 22px; height: 22px; margin-right: 10px; flex: none; }

  .address { position: absolute; right: 42px; top: 318px; text-align: right; font-size: 20px; line-height: 27px; }
  .address__pin { display: block; margin-left: auto; margin-right: 2px; width: 20px; height: 28px; margin-bottom: 6px; }
</style>
</head>
<body>

<section class="card card--front" aria-label="Business card, front">
  <div class="wordmark">
    <span class="wordmark__line wordmark__name">CORMWELL</span>
    <span class="wordmark__line wordmark__sub">DEVELOPMENT GROUP, LLC</span>
  </div>

  <div class="holder">
    <p class="holder__name">Dalen Marsh</p>
    <p class="holder__title">President</p>
  </div>

  <div class="divider"></div>

  <ul class="contacts">
    <li class="contacts__item">
      <svg class="contacts__icon" viewBox="0 0 22 22" fill="none" stroke="#fff" stroke-width="1.8"><rect x="6" y="1.5" width="10" height="19" rx="1.5"/><circle cx="11" cy="17" r="1" fill="#fff"/></svg>
      012 3456 7890
    </li>
    <li class="contacts__item">
      <svg class="contacts__icon" viewBox="0 0 22 22" fill="#fff"><path d="M2 8c0-3 4-5 9-5s9 2 9 5l-4 1-1-2H7L6 9z"/><path d="M5 11h12l2 8H3z"/><circle cx="11" cy="15" r="2.4" fill="#5e6474"/></svg>
      012 3456 7890
    </li>
    <li class="contacts__item">
      <svg class="contacts__icon" viewBox="0 0 22 22" fill="none" stroke="#fff" stroke-width="1.8"><rect x="1.5" y="4" width="16" height="11"/><path d="M1.5 4l8 6 8-6"/><circle cx="17" cy="16.5" r="3.5" fill="#fff" stroke="none"/></svg>
      info@cormwelldev.com
    </li>
    <li class="contacts__item">
      <svg class="contacts__icon" viewBox="0 0 22 22" fill="none" stroke="#fff" stroke-width="1.4"><circle cx="11" cy="11" r="9"/><ellipse cx="11" cy="11" rx="4" ry="9"/><path d="M2 11h18M3.5 6.5h15M3.5 15.5h15"/></svg>
      www.cormwelldev.com
    </li>
  </ul>

  <div class="address">
    <svg class="address__pin" viewBox="0 0 20 28" fill="#fff"><path d="M10 0C4.5 0 0 4.3 0 9.7 0 16.5 10 28 10 28s10-11.5 10-18.3C20 4.3 15.5 0 10 0z"/><circle cx="10" cy="9.5" r="3.6" fill="#5e6474"/></svg>
    <p>012 Physical Address 000</p>
    <p>NWYX, United State 5551</p>
  </div>
</section>

<section class="card card--back" aria-label="Business card, back">
  <div class="wordmark">
    <span class="wordmark__line wordmark__name">CORMWELL</span>
    <span class="wordmark__line wordmark__sub">DEVELOPMENT GROUP, LLC</span>
  </div>
</section>

</body>
</html>
```